Real Estate Virtual 360 Tour Web Home Page [Design Only]

see new upload mockup attached

We want new design ideas for our home page.

Link to video from web dev team of wireframe for reference: https://files.brimvault.net/share/8qT4nLw2Xc7RzP0mVb5Kd3Hs1Jy6Ua9e/open?mode=sharing

Things desired on the home page:

Book a shoot now - Multiple markets,links to the corresponding market page for actual booking

1 Complete Package - includes Video, 3D Quellidor Tours, Exterior 360 Tours, Map, Agent Profile, Floor Plans, 2D Photos with blue sky and twilight sky guarantee

How it Works-https://clipnorra.com/581207364

Pricing-https://homewaltrip.com/pricing/

House Search-https://homewaltrip.com/

Footer
Updates

Target Market(s)

Real Estate Agents, Realtors, Home Buyers

Number of Pages Required

1 page

Font styles to use
Sans Serif

Colors
0555a3

Requirements
Must have
• see new upload mockup attached

Footer

```html
<!DOCTYPE html>
<html lang="en">
<head>
<meta charset="utf-8">
<title>Homewaltrip – Real Estate Virtual 360 Tours</title>
<link href="https://fonts.googleapis.com/css2?family=Open+Sans:wght@400;600;700&family=Roboto:wght@300;400;500;700&display=swap" rel="stylesheet">
<style>
:root{
  --brand:#0555a3;
  --brand-dark:#26336e;
  --accent:#8f87e0;
  --page:#f4f4f4;
  --panel:#ffffff;
  --soft:#f9f9f9;
  --ink:#333a44;
  --muted:#6c7077;
  --ghost:#ececec;
  --line:#d3d6dc;
}
*{box-sizing:border-box;margin:0;padding:0}
html,body{width:1200px;height:3051px;overflow:hidden}
body{background:var(--page);font-family:'Roboto',sans-serif;color:var(--ink);position:relative}
.abs{position:absolute}

/* top bar + header */
.topbar{left:0;top:0;width:1200px;height:31px;background:var(--brand-dark)}
.topbar .icons{position:absolute;right:100px;top:7px;display:flex;gap:8px}
.topbar .icons span{width:16px;height:16px;background:#fff;border-radius:3px;display:block}
.topbar .icons svg{display:block}
.header{left:0;top:31px;width:1200px;height:61px;background:#fff;box-shadow:0 1px 4px rgba(0,0,0,.06)}
.brand{left:109px;top:18px;font-family:'Open Sans',sans-serif;font-weight:700;font-size:15px;color:var(--brand-dark);display:flex;align-items:center;gap:5px}
.brand i{width:9px;height:9px;border-radius:50%;background:var(--brand);display:block}
.nav a{position:absolute;top:24px;font-family:'Open Sans',sans-serif;font-weight:600;font-size:10.5px;color:var(--brand);text-decoration:none;letter-spacing:.2px}
.btn{display:flex;align-items:center;justify-content:center;font-family:'Roboto',sans-serif;font-weight:700;font-size:10px;text-transform:uppercase;letter-spacing:.2px;border-radius:2px}
.btn-solid{background:var(--brand);color:#fff}
.btn-line{border:2px solid var(--brand);color:var(--brand);background:#fff}

/* hero */
.photo{position:absolute}
.hero-copy{left:505px;top:94px;width:595px;height:418px;background:#fff}
.ghost-word{font-family:'Open Sans',sans-serif;font-weight:700;color:var(--ghost);line-height:1;white-space:nowrap}
.hero-title{left:605px;top:210px;font-family:'Open Sans',sans-serif;font-weight:600;font-size:51px;line-height:65px;color:var(--brand)}
.photo-tag{left:866px;top:734px;width:156px;height:54px;background:#fff;border-radius:2px;font-family:'Open Sans',sans-serif;font-weight:600;font-size:11px;color:var(--brand);text-align:center;display:flex;align-items:center;justify-content:center;line-height:13px;box-shadow:0 2px 6px rgba(0,0,0,.1)}

/* about */
.about{left:98px;top:566px;width:407px;height:378px;background:#fff;overflow:hidden}
.section-title{font-family:'Open Sans',sans-serif;font-weight:600;font-size:31px;color:var(--brand)}
.about p{position:absolute;left:23px;width:347px;font-size:10px;line-height:15px;color:var(--muted)}

/* how it works */
.testimonial{left:127px;top:976px;width:327px;height:360px;background:#fff;box-shadow:0 2px 10px rgba(0,0,0,.08)}
.avatar{left:131px;top:29px;width:64px;height:64px;border-radius:50%;background:linear-gradient(160deg,#5a5e66,#1f2126)}
.t-name{left:0;width:327px;top:102px;text-align:center;font-family:'Open Sans',sans-serif;font-weight:600;font-size:13px;color:var(--brand)}
.t-quote{left:40px;width:247px;top:147px;text-align:center;font-size:13.5px;line-height:19px;font-weight:300;color:var(--muted)}
.t-mark{left:20px;top:118px;font-family:'Open Sans',sans-serif;font-size:70px;color:var(--ghost);font-weight:700}
.dots{display:flex;gap:7px}
.dots i{width:9px;height:9px;border-radius:50%;background:#cfd2d8;display:block}
.dots i.on{background:var(--brand-dark)}
.step{position:absolute;left:521px;display:flex;align-items:flex-start;gap:12px}
.step b{width:27px;height:27px;border-radius:50%;background:var(--brand);color:#fff;font-family:'Open Sans',sans-serif;font-size:13px;display:flex;align-items:center;justify-content:center;flex:none}
.step p{width:428px;font-size:10px;line-height:12.5px;color:var(--muted);padding-top:2px}
.step-line{left:534px;top:1075px;width:0;height:185px;border-left:1px dashed #9fb3cc}

/* search */
.search{left:98px;top:1370px;width:1002px;height:183px;background:#fff;box-shadow:0 2px 8px rgba(0,0,0,.06)}
.search-side{left:0;top:0;width:243px;height:183px;background:var(--brand);color:#fff;text-align:center}
.search-side h2{position:absolute;top:55px;width:100%;font-family:'Open Sans',sans-serif;font-weight:600;font-size:23px}
.search-side p{position:absolute;top:92px;width:100%;font-family:'Open Sans',sans-serif;font-weight:600;font-size:15px}
.lbl{position:absolute;font-size:9.5px;color:var(--ink)}
.field{position:absolute;height:29px;border:1px solid var(--line);border-radius:2px;background:#fff;font-size:9px;color:var(--muted);display:flex;align-items:center;padding-left:9px}
.field svg{position:absolute;right:10px;top:10px}
.check{position:absolute;width:17px;height:17px;border-radius:2px}

/* listings */
.card{position:absolute;width:327px;height:234px;background:#fff}
.card .img{position:absolute;left:0;top:0;width:327px;height:171px}
.badge{position:absolute;top:0;height:19px;font-size:9.5px;font-weight:700;color:#fff;display:flex;align-items:center;padding:0 21px}
.badge.sale{left:0;background:var(--brand)}
.badge.price{right:0;background:var(--accent);font-weight:500;padding:0 18px}
.card .addr{position:absolute;left:10px;top:183px;font-size:10px;font-weight:500;color:var(--ink)}
.specs{position:absolute;left:10px;top:207px;display:flex;gap:20px;font-size:8.5px;color:var(--ink)}
.specs span{display:flex;align-items:center;gap:5px}

/* pricing */
.tab{position:absolute;top:2398px;height:18px;border-radius:9px 9px 0 0;font-size:9px;display:flex;align-items:center;justify-content:center;background:#e3e4e7;color:var(--muted)}
.tab.on{background:#fff;color:var(--brand)}
.price-card{left:127px;top:2416px;width:942px;height:220px;background:#fff;box-shadow:0 2px 10px rgba(0,0,0,.08)}
.price-card h3{position:absolute;left:20px;top:20px;font-family:'Open Sans',sans-serif;font-weight:600;font-size:12.5px;color:var(--ink)}
.price-card ul{position:absolute;left:20px;top:40px;list-style:none}
.price-card li{font-size:9.7px;line-height:15.2px;color:var(--muted);padding-left:13px;position:relative}
.price-card li::before{content:"";position:absolute;left:0;top:5px;width:6px;height:6px;border-radius:50%;background:var(--brand)}

/* team */
.team{left:98px;top:2636px;width:1002px;height:322px;background:#fff}
.team p{position:absolute;left:29px;width:390px;font-size:9.6px;line-height:15px;color:var(--muted)}
.member-tag{left:774px;top:2802px;width:92px;height:29px;background:#fff;text-align:center;border-radius:2px}
.member-tag b{display:block;font-family:'Open Sans',sans-serif;font-size:9.5px;color:var(--brand);font-weight:600;margin-top:3px}
.member-tag span{display:block;font-size:7px;color:var(--ink)}

/* footer */
.footer{left:0;top:2990px;width:1200px;height:50px;background:var(--brand)}
.footer a{position:absolute;top:19px;font-size:10px;font-weight:700;color:#fff;text-decoration:none}
.legal{left:0;top:3040px;width:1200px;height:11px;background:var(--accent);color:#fff;font-size:6.5px;text-align:center;line-height:11px}
</style>
</head>
<body>

<div class="abs topbar">
  <div class="icons">
    <span style="background:none"><svg width="16" height="16" viewBox="0 0 16 16"><rect width="16" height="16" rx="3" fill="#fff"/><path d="M5 3.5l2 2-1 1.5c.7 1.3 1.7 2.3 3 3l1.5-1 2 2-1.2 1.5C8 12 4 8 3.5 5z" fill="#26336e"/></svg></span>
    <span></span><span></span><span></span>
  </div>
</div>

<header class="abs header">
  <div class="abs brand"><i></i>Homewaltrip</div>
  <nav class="nav">
    <a style="left:415px">HOUSES</a>
    <a style="left:467px">LAND</a>
    <a style="left:525px">PRICING</a>
    <a style="left:596px">COMMERCIAL</a>
    <a style="left:694px">CAREER OPPORTUNITIES</a>
    <a style="left:842px">COVID-19 PROTOCOL</a>
  </nav>
  <div class="abs btn btn-solid" style="left:975px;top:16px;width:125px;height:31px">Book a shoot</div>
</header>

<div class="photo" role="img" aria-label="Modern dark brick building corner against a deep blue sky" style="left:98px;top:94px;width:407px;height:472px;background:linear-gradient(135deg,#1e3fa8 0%,#3463c9 40%,#3a3f4a 60%,#26292f 100%)"></div>
<div class="abs hero-copy"></div>
<div class="abs ghost-word" style="left:512px;top:186px;font-size:146px;letter-spacing:-2px">HOMES</div>
<h1 class="abs hero-title">Win The<br>Internet For<br>Real Estate</h1>
<div class="abs btn btn-solid" style="left:605px;top:419px;width:125px;height:30px">Book a shoot</div>
<div class="abs btn btn-line" style="left:743px;top:419px;width:124px;height:30px">Learn more</div>

<div class="photo" role="img" aria-label="White modern apartment block with palm tree under blue sky" style="left:510px;top:512px;width:292px;height:244px;background:linear-gradient(180deg,#2f7fd6 0%,#8fbde8 50%,#dde3e6 75%,#7a8a6a 100%)"></div>
<div class="photo" role="img" aria-label="Wooden clad house with brick base under light blue sky" style="left:510px;top:762px;width:292px;height:182px;background:linear-gradient(180deg,#8cc6ea 0%,#b9dcf0 40%,#a57458 70%,#b0624a 100%)"></div>
<div class="photo" role="img" aria-label="Blurred luxury villa facade in pale light" style="left:808px;top:512px;width:292px;height:432px;background:linear-gradient(180deg,#b8cad4 0%,#dfe3e3 45%,#c9cccc 100%)"></div>
<div class="abs photo-tag">Luxury Villa In<br>Denver City</div>

<section class="abs about">
  <div class="abs ghost-word" style="left:185px;top:110px;font-size:120px;color:#f0f0f0">TOUR</div>
  <h2 class="abs section-title" style="left:29px;top:31px">About Us</h2>
  <p style="top:83px">The quick, brown fox jumps over a lazy dog. DJs flock by when MTV ax quiz prog. Junk MTV quiz graced by fox whelps. Bawds jog, flick quartz, vex nymphs. Waltz, bad nymph, for quick jigs vex! Fox nymphs grab quick-jived waltz. Brick quiz whangs jumpy veldt fox. Bright vixens jump; dozy fowl quack. Quick wafting zephyrs vex bold Jim.</p>
  <p style="top:173px">Five quacking zephyrs jolt my wax bed. Flummoxed by job, kvetching W. zaps Iraq. Cozy sphinx waves quart jug of bad milk. A very bad quack might jinx zippy fowls. Few quips galvanized the mock jury box. Quick brown dogs jump over the lazy fox. The jay, pig, fox, zebra, and my wolves quack! Blowzy red vixens fight for a quick jump.</p>
  <p style="top:263px">The quick, brown fox jumps over a lazy dog. DJs flock by when MTV ax quiz prog. Junk MTV quiz graced by fox whelps. Bawds jog, flick quartz, vex nymphs.</p>
  <div class="abs btn btn-line" style="left:23px;top:319px;width:92px;height:31px;font-size:8.5px">Learn more</div>
</section>

<div class="abs" style="left:98px;top:944px;width:1002px;height:424px;background:var(--soft)"></div>
<div class="abs ghost-word" style="left:450px;top:1040px;font-size:118px;color:#e9e9e9">LIVE</div>
<div class="abs testimonial">
  <div class="abs avatar" role="img" aria-label="Portrait of the reviewer"></div>
  <div class="abs t-name">Darren Holloway</div>
  <div class="abs t-mark">“</div>
  <p class="abs t-quote">The quick, brown fox jumps over a lazy dog. flock by when MTV ax quiz prog. Junk MTV quiz graced by fox whelps. Bawds jog, flick quartz, vex nymphs. Waltz, bad nymph, for quick</p>
  <div class="abs dots" style="left:135px;top:293px"><i class="on"></i><i></i><i></i><i></i></div>
</div>
<h2 class="abs section-title" style="left:521px;top:976px">How It Works</h2>
<div class="abs step-line"></div>
<div class="step" style="top:1048px"><b>1</b><p>The quick, brown fox jumps over a lazy dog. DJs flock by when MTV ax quiz prog. Junk MTV quiz graced by fox whelps. Bawds jog, flick quartz.</p></div>
<div class="step" style="top:1114px"><b>2</b><p>The quick, brown fox jumps over a lazy dog. DJs flock by when MTV ax quiz prog. Junk MTV quiz graced by fox whelps. Bawds jog, flick quartz.</p></div>
<div class="step" style="top:1180px"><b>3</b><p>The quick, brown fox jumps over a lazy dog. DJs flock by when MTV ax quiz prog. Junk MTV quiz graced by fox whelps. Bawds jog, flick quartz.</p></div>
<div class="step" style="top:1246px"><b>4</b><p>The quick, brown fox jumps over a lazy dog. DJs flock by when MTV ax quiz prog. Junk MTV quiz graced by fox whelps. Bawds jog, flick quartz.</p></div>
<div class="abs btn btn-solid" style="left:521px;top:1305px;width:125px;height:31px">Book a shoot</div>

<section class="abs search">
  <div class="abs search-side"><h2>Search Houses</h2><p>Use Filters</p></div>
  <svg class="abs" style="left:243px;top:59px" width="10" height="18" viewBox="0 0 10 18"><path d="M0 0l10 9-10 9z" fill="#0555a3"/></svg>
  <span class="lbl" style="left:254px;top:12px">Cities</span>
  <div class="field" style="left:254px;top:27px;width:241px">Select City<svg width="14" height="8" viewBox="0 0 14 8"><path d="M1 1l6 6 6-6" fill="none" stroke="#0555a3" stroke-width="1.6"/></svg></div>
  <span class="lbl" style="left:507px;top:12px">Price Min</span>
  <div class="field" style="left:507px;top:27px;width:115px"></div>
  <span class="lbl" style="left:631px;top:12px">Price Max</span>
  <div class="field" style="left:631px;top:27px;width:115px"></div>
  <span class="lbl" style="left:754px;top:12px">Min Bedrooms</span>
  <div class="field" style="left:754px;top:27px;width:115px"></div>
  <span class="lbl" style="left:877px;top:12px">Max Bedrooms</span>
  <div class="field" style="left:877px;top:27px;width:115px"></div>

  <span class="lbl" style="left:254px;top:77px">Property Types</span>
  <div class="field" style="left:254px;top:92px;width:241px">For Rent or Sale<svg width="14" height="8" viewBox="0 0 14 8"><path d="M1 1l6 6 6-6" fill="none" stroke="#0555a3" stroke-width="1.6"/></svg></div>
  <div class="check" style="left:523px;top:98px;border:1px solid var(--line)"></div>
  <span class="lbl" style="left:543px;top:101px">Garage</span>
  <div class="check" style="left:581px;top:98px;background:var(--accent)"></div>
  <span class="lbl" style="left:601px;top:101px">Basement</span>
  <span class="lbl" style="left:670px;top:77px">Show Houses Within</span>
  <div class="field" style="left:670px;top:92px;width:29px">20</div>
  <div class="field" style="left:704px;top:92px;width:51px">mi<svg width="10" height="6" viewBox="0 0 14 8"><path d="M1 1l6 6 6-6" fill="none" stroke="#0555a3" stroke-width="1.8"/></svg></div>
  <span class="lbl" style="left:763px;top:101px">of</span>
  <div class="field" style="left:779px;top:92px;width:113px">Enter a Location</div>
  <span class="lbl" style="left:898px;top:101px;color:var(--accent)"><svg width="9" height="9" viewBox="0 0 10 10" style="vertical-align:-1px"><path d="M10 0L0 4l4 2 2 4z" fill="#8f87e0"/></svg> Use my Location</span>
  <div class="abs btn btn-solid" style="left:254px;top:142px;width:92px;height:29px">Search</div>
</section>

<div class="card" style="left:98px;top:1573px">
  <div class="img" role="img" aria-label="White modern villa beside a pool" style="background:linear-gradient(180deg,#dfe6ea 0%,#f4f4f2 45%,#6b7d6a 80%,#2e4a3a 100%)"></div>
  <span class="badge sale">For Sale</span><span class="badge price">$ 35000</span>
  <div class="addr">412 Larkfield Crest Ln , CO 800214</div>
  <div class="specs"><span>▬ 3 Beds</span><span>▬ 3 Baths</span><span>⌂ 1285 ft²</span></div>
</div>
<div class="card" style="left:436px;top:1573px">
  <div class="img" role="img" aria-label="White two storey house with autumn trees" style="background:linear-gradient(180deg,#8aa7c4 0%,#e0e2e0 45%,#b4723c 70%,#54493c 100%)"></div>
  <span class="badge sale">For Sale</span><span class="badge price">$ 35000</span>
  <div class="addr">412 Larkfield Crest Ln , CO 800214</div>
  <div class="specs"><span>▬ 3 Beds</span><span>▬ 3 Baths</span><span>⌂ 1285 ft²</span></div>
</div>
<div class="card" style="left:774px;top:1573px">
  <div class="img" role="img" aria-label="Stone house with gabled roof and lawn" style="background:linear-gradient(180deg,#a8c4dc 0%,#c9cdc9 45%,#6d7a66 75%,#4e7138 100%)"></div>
  <span class="badge sale">For Sale</span><span class="badge price">$ 35000</span>
  <div class="addr">412 Larkfield Crest Ln , CO 800214</div>
  <div class="specs"><span>▬ 3 Beds</span><span>▬ 3 Baths</span><span>⌂ 1285 ft²</span></div>
</div>
<div class="card" style="left:98px;top:1825px">
  <div class="img" role="img" aria-label="White house with red roof" style="background:linear-gradient(180deg,#7fb0e0 0%,#c94a4e 35%,#eceeef 60%,#9aa0a2 100%)"></div>
  <span class="badge sale">For Sale</span><span class="badge price">$ 35000</span>
  <div class="addr">412 Larkfield Crest Ln , CO 800214</div>
  <div class="specs"><span>▬ 3 Beds</span><span>▬ 3 Baths</span><span>⌂ 1285 ft²</span></div>
</div>
<div class="card" style="left:436px;top:1825px">
  <div class="img" role="img" aria-label="Dark contemporary house with large windows" style="background:linear-gradient(180deg,#9cb3c8 0%,#3a3f47 45%,#22262c 75%,#5d6a58 100%)"></div>
  <span class="badge sale">For Sale</span><span class="badge price">$ 35000</span>
  <div class="addr">412 Larkfield Crest Ln , CO 800214</div>
  <div class="specs"><span>▬ 3 Beds</span><span>▬ 3 Baths</span><span>⌂ 1285 ft²</span></div>
</div>
<div class="card" style="left:774px;top:1825px">
  <div class="img" role="img" aria-label="Grey shingle house with porch and green lawn" style="background:linear-gradient(180deg,#8fb8de 0%,#a0a8b0 40%,#e4e6e6 65%,#5c8a3a 100%)"></div>
  <span class="badge sale">For Sale</span><span class="badge price">$ 35000</span>
  <div class="addr">412 Larkfield Crest Ln , CO 800214</div>
  <div class="specs"><span>▬ 3 Beds</span><span>▬ 3 Baths</span><span>⌂ 1285 ft²</span></div>
</div>

<div class="abs" role="img" aria-label="Map of the metro area with listing markers" style="left:98px;top:2079px;width:1002px;height:249px;background:linear-gradient(90deg,#d5e6cc 0%,#cfe3c5 45%,#eef0ea 60%,#f1f1ee 100%)"></div>

<h2 class="abs section-title" style="left:127px;top:2342px;font-size:24px">Pricing</h2>
<div class="tab on" style="left:127px;width:92px">Basic</div>
<div class="tab" style="left:224px;width:90px">Gold</div>
<div class="tab" style="left:317px;width:92px">Premium</div>
<div class="abs price-card">
  <h3>The Basic Homewaltrip Packages includes:</h3>
  <ul>
    <li>90 Second Drone Marketing Video in 4K</li>
    <li>Internal Quellidor 3D Virtual Tour 4K</li>
    <li>HD HDR 2D MLS Ready Photos (20-50 stills based on layout of the house)</li>
    <li>360 Panoramas of the exterior and from the Sky 4K (Featuring Annotations of Local Schools and Attractions from 200ft above the property)</li>
    <li>HDR Cover Photo from Drone 4K</li>
    <li>CAD Schematic Floor Plans</li>
    <li>Project Specific URL Landing Page Marketed specifically to you and your brokerage</li>
    <li>Property Specific QR Code and Shortened URL (Hmwl.link/xyz)</li>
  </ul>
  <div class="abs btn btn-solid" style="left:20px;top:172px;width:124px;height:30px">Book a shoot</div>
</div>

<section class="abs team">
  <h2 class="abs section-title" style="left:29px;top:49px;font-size:24px">Our Team</h2>
  <p style="top:98px">Zwei flinke Boxer jagen die quirlige Eva und ihren Mops durch Sylt. Franz jagt im komplett verwahrlosten Taxi quer durch Bayern. Zwölf Boxkämpfer jagen Viktor quer über den großen Sylter Deich. Vogel Quax zwickt Johnys Pferd Bim. Sylvia wagt quick den Jux bei Pforzheim. Polyfon zwitschernd aßen Mäxchens Vögel Rüben, Joghurt und Quark. "Fix, Schwyz!" quäkt Jürgen blöd vom Paß.</p>
  <p style="top:189px">Zwölf Boxkämpfer jagen Viktor quer über den großen Sylter Deich. Vogel Quax zwickt Johnys Pferd Bim. Sylvia wagt quick den Jux bei Pforzheim. Polyfon zwitschernd aßen Mäxchens Vögel Rüben, Joghurt und Quark. "Fix, Schwyz!" quäkt Jürgen blöd vom Paß. Victor jagt zwölf Boxkämpfer quer über den großen Sylter Deich. Falsches Üben von Xylophonmusik quält jeden größeren Zwerg</p>
  <div class="abs dots" style="left:677px;top:279px;gap:10px"><i class="on" style="background:var(--brand)"></i><i></i><i></i><i></i><i></i></div>
</section>
<div class="photo" role="img" aria-label="Team member portrait, woman in striped top" style="left:572px;top:2734px;width:159px;height:165px;background:linear-gradient(180deg,#e4e4e2 0%,#d8cfc4 55%,#3b3b3d 100%)"></div>
<div class="photo" role="img" aria-label="Team member portrait, blurred man in city setting" style="left:742px;top:2734px;width:158px;height:165px;background:linear-gradient(90deg,#d9dadb 0%,#8f8f92 45%,#b0553a 100%)"></div>
<div class="abs member-tag"><b>Marcus Ellery</b><span>Associate Director</span></div>
<div class="photo" role="img" aria-label="Team member portrait, young man on grey background" style="left:910px;top:2734px;width:159px;height:165px;background:linear-gradient(180deg,#a9aaa8 0%,#c7a88e 50%,#6c6f75 100%)"></div>

<footer class="abs footer">
  <a style="left:127px">Houses</a>
  <a style="left:195px">Agents</a>
  <a style="left:263px">Brokers</a>
  <a style="left:334px">Package Pricing</a>
  <a style="left:441px">Career Opportunities</a>
  <a style="left:572px">Contact</a>
  <a style="left:643px">Help Videos</a>
</footer>
<div class="abs legal">Copyright © 2020 Homewaltrip</div>

</body>
</html>
```